An advertising banner 8ft by 4ft

The advertising banner is going on a building to advertise my company's products and services,we install burglar alarms and CCTV systems, please check out our website for the company logo www.corvellan.co.uk and a general theme of what we do.

We are big on control your alarm and CCTV with your smartphone so my be a phone in hand will be good.

I have been established since 1982

Target Market(s)

Home Security, CCTV and burglar alarms

Industry/Entity Type

Security Service

Colors
9bcb3c

Requirements
Must have
• Pictures of CCTV and alarms system our telephone number 0151 637 2184 and our website www.corvellan.co.uk
• Our Company name: Corvellan Security Systems Ltd
• Our Address: Unit 7 Ashgrove Business Park, Pellinor Road, Widnes WA8 3KP
Nice to have
• Check out the following website to have a look at the produces we use (these are our suppliers) https://www.tavelix.co.uk/
• Our building its on the website

```html
<!DOCTYPE html>
<html lang="en">
<head>
<meta charset="utf-8">
<title>Corvellan Security Systems – Building Banner</title>
<link rel="stylesheet" href="https://fonts.googleapis.com/css2?family=Open+Sans:wght@400;600;700;800&display=swap">
<style>
  :root {
    --brand-green: #8cc21f;
    --ink: #3a3a3a;
    --ink-soft: #555555;
    --band-grey: #5b5b5b;
    --page: #ececec;
    --white: #ffffff;
  }
  * { margin: 0; padding: 0; box-sizing: border-box; }
  html, body {
    width: 833px; height: 1200px; overflow: hidden;
    background: var(--page);
    font-family: "Open Sans", Arial, sans-serif;
  }
  .banner {
    position: absolute; left: 126px; top: 20px;
    width: 580px; height: 1160px;
    background: radial-gradient(ellipse at 50% 20%, #ffffff 0%, #f4f4f4 100%);
    box-shadow: 0 4px 14px rgba(0,0,0,.18);
    overflow: hidden;
  }
  .top-band { position: absolute; left: 0; top: 0; width: 100%; height: 16px; background: var(--brand-green); }
  .brand { position: absolute; top: 78px; width: 100%; text-align: center; }
  .brand-name { font-size: 64px; font-weight: 800; color: var(--ink-soft); letter-spacing: 1px; line-height: 1; }
  .brand-sub { margin-top: 24px; font-size: 24px; font-weight: 400; color: var(--ink-soft); letter-spacing: 4px; }
  .headline { position: absolute; top: 232px; width: 100%; text-align: center;
    font-size: 34px; line-height: 40px; color: var(--ink); font-weight: 400; }
  .headline strong { font-weight: 800; }
  .headline .accent { color: var(--brand-green); font-weight: 800; }
  .diagram { position: absolute; left: 0; top: 0; }
  .diagram-label { font-family: "Open Sans", Arial, sans-serif; font-size: 17px; font-weight: 700; fill: var(--ink); }
  .smartphone-note { position: absolute; top: 918px; width: 100%; text-align: center;
    font-size: 23px; line-height: 34px; color: var(--ink); }
  .smartphone-note b { color: var(--brand-green); font-weight: 800; }
  .address { position: absolute; top: 956px; width: 100%; text-align: center;
    font-size: 17px; line-height: 30px; color: var(--ink); }
  .service-band { position: absolute; top: 996px; left: 0; width: 100%; height: 52px;
    background: var(--band-grey); color: var(--white); text-align: center;
    font-size: 29px; font-weight: 700; line-height: 52px; letter-spacing: .5px; }
  .contact-band { position: absolute; top: 1048px; left: 0; width: 100%; height: 112px;
    background: var(--brand-green); color: var(--white); text-align: center; }
  .contact-phone { margin-top: 6px; font-size: 50px; font-weight: 800; line-height: 60px; }
  .contact-phone svg { vertical-align: -4px; margin-right: 10px; }
  .contact-email { font-size: 34px; font-weight: 400; line-height: 40px; }
  .contact-email b { font-weight: 700; }
  .contact-email svg { vertical-align: -3px; margin-right: 10px; }
</style>
</head>
<body>
<div class="banner">
  <div class="top-band"></div>

  <div class="brand">
    <div class="brand-name">Corvellan</div>
    <div class="brand-sub">Security Systems Ltd</div>
  </div>

  <h1 class="headline">WE ARE <strong>BIG</strong> ON CONTROL YOUR<br>
    <span class="accent">ALARM</span> AND <span class="accent">CCTV</span></h1>

  <svg class="diagram" width="580" height="1160" viewBox="0 0 580 1160">
    <defs>
      <linearGradient id="keypad-tone" x1="0" y1="0" x2="1" y2="1">
        <stop offset="0" stop-color="#e8eef6"/><stop offset="1" stop-color="#8ea3c4"/>
      </linearGradient>
      <linearGradient id="fob-tone" x1="0" y1="0" x2="1" y2="1">
        <stop offset="0" stop-color="#e9c9b0"/><stop offset="1" stop-color="#2e2e2e"/>
      </linearGradient>
      <linearGradient id="panel-tone" x1="0" y1="0" x2="1" y2="1">
        <stop offset="0" stop-color="#f2f2f2"/><stop offset="1" stop-color="#9fb1d0"/>
      </linearGradient>
      <linearGradient id="wireless-tone" x1="0" y1="0" x2="1" y2="1">
        <stop offset="0" stop-color="#5a5a5a"/><stop offset="1" stop-color="#151515"/>
      </linearGradient>
      <linearGradient id="app-tone" x1="0" y1="0" x2="1" y2="1">
        <stop offset="0" stop-color="#e2b999"/><stop offset="1" stop-color="#2a2a2a"/>
      </linearGradient>
    </defs>

    <g class="connectors" stroke="var(--brand-green)" stroke-width="46" stroke-linecap="round">
      <line x1="301" y1="609" x2="125" y2="442"/>
      <line x1="301" y1="609" x2="466" y2="442"/>
      <line x1="301" y1="609" x2="133" y2="780"/>
      <line x1="301" y1="609" x2="471" y2="780"/>
    </g>

    <g class="rings" fill="var(--brand-green)">
      <circle cx="125" cy="442" r="80"/>
      <circle cx="466" cy="442" r="80"/>
      <circle cx="301" cy="609" r="74"/>
      <circle cx="133" cy="780" r="80"/>
      <circle cx="471" cy="780" r="80"/>
    </g>

    <g role="img" aria-label="Photo of alarm keypads">
      <circle cx="125" cy="442" r="67" fill="url(#keypad-tone)"/>
    </g>
    <g role="img" aria-label="Photo of a hand holding a keyfob">
      <circle cx="466" cy="442" r="67" fill="url(#fob-tone)"/>
    </g>
    <g role="img" aria-label="Photo of the alarm control panel">
      <circle cx="301" cy="609" r="61" fill="url(#panel-tone)"/>
    </g>
    <g role="img" aria-label="Photo of a wireless alarm sensor">
      <circle cx="133" cy="780" r="67" fill="url(#wireless-tone)"/>
    </g>
    <g role="img" aria-label="Photo of a hand holding a smartphone with the alarm app">
      <circle cx="471" cy="780" r="67" fill="url(#app-tone)"/>
    </g>

    <text class="diagram-label" x="122" y="350" text-anchor="middle">Keypad</text>
    <text class="diagram-label" x="470" y="350" text-anchor="middle">Keyfobs</text>
    <text class="diagram-label" x="301" y="749" text-anchor="middle">Control Panel</text>
    <text class="diagram-label" x="115" y="893" text-anchor="middle">Wireless</text>
    <text class="diagram-label" x="474" y="893" text-anchor="middle">App</text>
  </svg>

  <p class="smartphone-note">WITH YOUR <b>SMARTPHONE</b></p>
  <p class="address">Unit 7 Ashgrove Business Park, Pellinor Road, Widnes WA8 3KP</p>

  <div class="service-band">COMMERCIAL ALARM SYSTEMS</div>

  <div class="contact-band">
    <div class="contact-phone">
      <svg width="34" height="34" viewBox="0 0 24 24" aria-hidden="true"><path fill="none" stroke="#fff" stroke-width="2" stroke-linejoin="round" d="M6 3l3 4-2 2c1 3 4 6 7 7l2-2 4 3-2 4C10 21 3 14 3 5z"/><path fill="none" stroke="#fff" stroke-width="1.6" d="M14 3a7 7 0 0 1 7 7M14 7a3 3 0 0 1 3 3"/></svg>0151 637 2184
    </div>
    <div class="contact-email">
      <svg width="26" height="26" viewBox="0 0 24 24" aria-hidden="true"><circle cx="12" cy="12" r="10" fill="none" stroke="#fff" stroke-width="2"/><path fill="none" stroke="#fff" stroke-width="1.5" d="M2 12h20M12 2c3 3 3 17 0 20M12 2c-3 3-3 17 0 20M4 7h16M4 17h16"/></svg>help@<b>corvellan</b>.co.uk
    </div>
  </div>
</div>
</body>
</html>
```